Business Card - Rebranding for Consulting Firm

We are renaming and rebranding our consulting firm and need to raise the level of quality of our cards as part of that effort. We consult to leading high tech, life science and other innovation sector companies.

Need a two-sided business card design.

Side 1: (a) Company logo (b) tag line: Optimize Your Investment in Talent (c) Name (d) Title (e) Phone 1: Office (f) Phone 2: Mobile (g) email: person@HollowmereAdvisory.com

Side 2: Two lines of text: (a) Growth is Imperative. Change is Constant. Talent Executes Strategy. (b) We help you excel at all three.

Target Market(s)

Business and human resources executives and senior managers

Industry/Entity Type

Management Consulting

Contact Information for Business Card

Font styles to use
Sans Serif

Requirements
Must have
• clean, not too busy, but with a bit of creativity. Stick to the colors used in the attached logo
• appeal to high tech, life science companies
Nice to have
• prefer white background

```html
<!DOCTYPE html>
<html lang="en">
<head>
<meta charset="utf-8">
<title>Hollowmere Advisory – Business Card</title>
<link rel="stylesheet" href="https://fonts.googleapis.com/css2?family=Roboto:wght@400;500;700&display=swap">
<style>
  :root {
    --page-bg: #e6e8eb;
    --brand-deep: #0a66a0;
    --brand-mid: #1089bd;
    --brand-light: #1aa6de;
    --brand-ink: #0f5f99;
    --text-gray: #555b60;
    --white: #ffffff;
  }
  * { margin: 0; padding: 0; box-sizing: border-box; }
  html, body {
    width: 1200px; height: 1000px; overflow: hidden;
    background: var(--page-bg);
    font-family: "Roboto", Arial, sans-serif;
  }
  .card {
    position: absolute; left: 220px; width: 760px;
    box-shadow: 0 3px 10px rgba(0,0,0,.25);
    overflow: hidden;
  }
  .card-front {
    top: 50px; height: 433px;
    background: linear-gradient(120deg, var(--brand-deep) 0%, #0b6aa3 55%, #1677ad 100%);
    color: var(--white);
  }
  .card-back { top: 524px; height: 435px; background: var(--white); }
  .corner-accent { position: absolute; left: 0; top: 0; width: 760px; height: 100%; }

  .statement {
    position: absolute; top: 179px; left: 0; width: 100%;
    text-align: center; font-size: 19px; letter-spacing: .5px; line-height: 36px;
  }
  .statement .divider { color: var(--brand-light); margin: 0 9px; }

  .brand { position: absolute; left: 54px; top: 54px; display: flex; align-items: center; gap: 12px; }
  .brand-mark { width: 20px; height: 20px; background: var(--brand-ink); }
  .brand-name { font-size: 36px; font-weight: 400; color: var(--brand-ink); letter-spacing: -.3px; }
  .tagline {
    position: absolute; left: 54px; top: 126px;
    font-size: 18px; color: var(--brand-light); letter-spacing: 2.7px;
  }
  .person { position: absolute; left: 54px; top: 216px; }
  .person-name { font-size: 24px; font-weight: 700; color: var(--brand-ink); letter-spacing: .2px; }
  .person-title { font-size: 18px; color: var(--text-gray); letter-spacing: .6px; }
  .contacts { position: absolute; left: 54px; top: 290px; list-style: none; }
  .contacts li {
    display: flex; align-items: center; gap: 7px;
    font-size: 18px; color: var(--text-gray); height: 24.5px; letter-spacing: .6px;
  }
  .contacts svg { width: 13px; height: 13px; fill: var(--brand-light); flex: none; }
</style>
</head>
<body>

<section class="card card-front">
  <svg class="corner-accent" viewBox="0 0 760 433" role="img" aria-label="Decorative corner accent in brand blues">
    <defs>
      <linearGradient id="front-accent-fill" x1="0" y1="0" x2="1" y2="0">
        <stop offset="0" stop-color="#e9f3fa"/>
        <stop offset="1" stop-color="var(--brand-light)"/>
      </linearGradient>
    </defs>
    <polygon points="0,278 318,433 0,433" fill="url(#front-accent-fill)"/>
  </svg>
  <div class="statement">
    <p>Growth is Imperative<span class="divider">|</span>Change is Constant<span class="divider">|</span>Talent Executes Strategy</p>
    <p>We help you excel at all three.</p>
  </div>
</section>

<section class="card card-back">
  <svg class="corner-accent" viewBox="0 0 760 435" role="img" aria-label="Decorative corner accent in brand blues">
    <defs>
      <linearGradient id="back-accent-fill" x1="0" y1="0" x2="1" y2="0">
        <stop offset="0" stop-color="var(--brand-light)"/>
        <stop offset="1" stop-color="var(--brand-deep)"/>
      </linearGradient>
    </defs>
    <polygon points="760,284 450,435 760,435" fill="url(#back-accent-fill)"/>
  </svg>

  <div class="brand">
    <span class="brand-mark"></span>
    <span class="brand-name">Hollowmere Advisory LLC</span>
  </div>
  <p class="tagline">Optimize Your Investment in Talent</p>

  <div class="person">
    <p class="person-name">Marcus Ellwood</p>
    <p class="person-title">National Director</p>
  </div>

  <ul class="contacts">
    <li><svg viewBox="0 0 16 16"><path d="M4 0h8a1 1 0 0 1 1 1v14a1 1 0 0 1-1 1H4a1 1 0 0 1-1-1V1a1 1 0 0 1 1-1zm1 2v10h6V2zm3 11a1 1 0 1 0 0 2 1 1 0 0 0 0-2z"/></svg>0123 456 789</li>
    <li><svg viewBox="0 0 16 16"><path d="M3.6 1.2 6 3.6 4.6 5.8a10 10 0 0 0 5.6 5.6L12.4 10l2.4 2.4-1.8 2.4C7 14.2 1.8 9 1.2 3z"/></svg>0123 456 789</li>
    <li><svg viewBox="0 0 16 16"><path d="M0 3h16v1L8 9 0 4zm0 3 8 5 8-5v7H0z"/></svg>person@HollowmereAdvisory.com</li>
    <li><svg viewBox="0 0 16 16"><path d="M8 0a8 8 0 1 0 0 16A8 8 0 0 0 8 0zm-1 1.6V5H4.3A6.5 6.5 0 0 1 7 1.6zm2 0A6.5 6.5 0 0 1 11.7 5H9zM1.6 7H7v2H1.6a6.5 6.5 0 0 1 0-2zM9 7h5.4a6.5 6.5 0 0 1 0 2H9zm-4.7 4H7v3.4A6.5 6.5 0 0 1 4.3 11zM9 11h2.7A6.5 6.5 0 0 1 9 14.4z"/></svg>www.HollowmereAdvisory.com</li>
  </ul>
</section>

</body>
</html>
```